K & M Wheel Depot business cards

need business card for tire/car care company based in tampa, florida. we sell used and new tires, also we service vehicles, tune ups, oil chasnge, brakes and A/c we offer free towing with major vehicle repair and tire purchase. we also offer free estimates on any engine or a/c repair. also we have the lowest price in the city on used and new tires.

Contact Information for Business Card

4170 E Marigold Blvd,
Tampa, Fl 33581
Ph: 813-572-3186
KandMWheelDepot@Mailverse.com

Font styles to use
Serif
Sans Serif
Decorative

Requirements
Must have
• my logo, what we do ( used and new tires , oil change, brakes, tune ups, free towing vehicl. Also business info.
Nice to have
• an image of a towing truck, highlighting that we offer free towing. something close to what i have in one of the attached image

```html
<!DOCTYPE html>
<html lang="en">
<head>
<meta charset="utf-8">
<title>K &amp; M Wheel Depot – Business Cards</title>
<link rel="stylesheet" href="https://fonts.googleapis.com/css2?family=Open+Sans:wght@400;600;700&display=swap">
<style>
  :root {
    --backdrop: #e9e7e4;
    --steel-light: #e4e5e6;
    --steel-mid: #c9cacc;
    --steel-dark: #a9abae;
    --navy: #1f3266;
    --ink: #2b2b2b;
    --icon-dark: #1a1a1a;
  }
  * { margin: 0; padding: 0; box-sizing: border-box; }
  html, body { width: 1200px; height: 1000px; overflow: hidden; }
  body {
    background: var(--backdrop);
    font-family: "Open Sans", Arial, sans-serif;
    position: relative;
  }
  .card {
    position: absolute;
    left: 265px;
    width: 665px;
    height: 398px;
    background: linear-gradient(100deg, var(--steel-dark) 0%, var(--steel-light) 38%, var(--steel-mid) 62%, var(--steel-light) 82%, var(--steel-dark) 100%);
    box-shadow: 0 4px 14px rgba(0,0,0,0.25);
  }
  .card--front { top: 73px; }
  .card--back { top: 532px; }

  .brand {
    position: absolute;
    display: flex;
    align-items: center;
    gap: 12px;
    color: var(--navy);
    font-weight: 700;
    white-space: nowrap;
  }
  .brand__dot {
    width: 26px; height: 26px;
    border-radius: 50%;
    background: var(--navy);
    flex: none;
  }
  .card--front .brand { left: 40px; top: 188px; font-size: 31px; }
  .card--back .brand { left: 0; right: 0; justify-content: center; top: 176px; font-size: 40px; }
  .card--back .brand__dot { width: 32px; height: 32px; }

  .contact { position: absolute; left: 394px; top: 98px; width: 260px; }
  .contact__headline {
    color: var(--navy);
    font-weight: 700;
    font-size: 17px;
    margin-left: 4px;
  }
  .tow-truck {
    display: block;
    margin-top: 8px;
    width: 190px;
    height: 52px;
    background: linear-gradient(90deg, #3a3a3a, var(--icon-dark));
    border-radius: 6px;
  }
  .contact__address {
    margin-top: 28px;
    font-size: 14.5px;
    line-height: 22px;
    color: var(--ink);
  }
  .contact__line {
    display: flex;
    align-items: center;
    gap: 8px;
    font-size: 14.5px;
    line-height: 22px;
    color: var(--ink);
  }
  .contact__line:first-of-type { margin-top: 6px; }
  .contact__line svg { width: 12px; height: 12px; fill: var(--navy); flex: none; }

  .services {
    position: absolute;
    left: 0; right: 0; bottom: 25px;
    text-align: center;
    color: var(--navy);
    font-weight: 700;
    font-size: 15.5px;
    letter-spacing: -0.2px;
  }
</style>
</head>
<body>
  <section class="card card--front">
    <div class="brand"><span class="brand__dot"></span>K &amp; M Wheel Depot</div>
    <div class="contact">
      <p class="contact__headline">FREE TOWING</p>
      <div class="tow-truck" role="img" aria-label="Tow truck pulling a car"></div>
      <p class="contact__address">4170 E Marigold Blvd,<br>Tampa, Fl 33581</p>
      <p class="contact__line">
        <svg viewBox="0 0 24 24"><path d="M6.6 10.8a15.1 15.1 0 0 0 6.6 6.6l2.2-2.2a1 1 0 0 1 1-.25 11.4 11.4 0 0 0 3.6.57 1 1 0 0 1 1 1V20a1 1 0 0 1-1 1A17 17 0 0 1 3 4a1 1 0 0 1 1-1h3.5a1 1 0 0 1 1 1c0 1.25.2 2.45.57 3.57a1 1 0 0 1-.25 1z"/></svg>
        813-572-3186
      </p>
      <p class="contact__line">
        <svg viewBox="0 0 24 24"><path d="M2 5h20v14H2z M2 5l10 8 10-8" fill="none" stroke="#1f3266" stroke-width="2"/><path d="M2 5h20l-10 8z"/></svg>
        KandMWheelDepot@Mailverse.com
      </p>
    </div>
  </section>

  <section class="card card--back">
    <div class="brand"><span class="brand__dot"></span>K &amp; M Wheel Depot</div>
    <p class="services">USED AND NEW TIRES , OIL CHANGE, BRAKES, TUNE UPS, FREE TOWING VEHICLE</p>
  </section>
</body>
</html>
```